Motivational Poster Series for Students at Truck Driving School

We are looking for a series of 3 motivational posters (18"X 24") to be used in classrooms at a truck driving school. The audience for the posters will be the students that are currently in school and the purpose of the posters is to be motivational pieces that will be displayed on the walls.

We have provided the quotes below that are to be used on each poster. We have also provided some example images from PixQuarry to give an idea on the backgrounds that we'd like to see on each poster. The images do not have to be exact, these are just examples of what we think will look good for each quote. Since this is a series, they can all be somewhat similar in look/feel - just with different images and quotes.

So, the basic idea is a background image/design with a quote being the main point of emphasis. Other than that, we would like to include the logo provided at a small scale in one of the corners of the poster as a watermark for branding purposes.

Below are the quotes for each of the 3 posters:

Poster 1 - “It’s very difficult to follow our dreams, but it’s even more difficult to forget them.” - Devan Kollur

Poster 2 - “Success doesn’t just come and find you, you have to go out and get it.” - Unknown

Poster 3 - “If you are not willing to learn, no one can help you. If you are determined to learn, no one can stop you.”
- Unknown

NOTE: these posters should be designed as 18" X 24" in size with 2 of them being landscape and one being portrait orientation (as shown in images provided below)

Below are some sample images to give an idea on what could be used as background design for each quote. The logo that should be used as a watermark in a corner for some subtle branding has been provided as well.

Target Market(s)

The target market for this series are truck drivers between the ages of 25-55. Mostly males.

Industry/Entity Type

Landscape

Requirements
Must have
• Quote featured, high quality background design/image, logo watermark

```html
<!DOCTYPE html>
<html lang="en">
<head>
<meta charset="utf-8">
<title>Motivational Poster – Follow Our Dreams</title>
<link rel="stylesheet" href="https://fonts.googleapis.com/css2?family=Questrial&display=swap">
<style>
  :root {
    --sky-top: #e9a43c;
    --sky-mid: #f0953a;
    --sky-low: #e7833d;
    --ground: #d9743a;
    --ink: #141010;
    --accent: #8f1d1d;
    --mark: #ffffff;
  }
  html, body {
    margin: 0;
    padding: 0;
    overflow: hidden;
    background: #ffffff;
  }
  .poster {
    position: relative;
    width: 1200px;
    height: 900px;
    overflow: hidden;
    font-family: "Questrial", "Helvetica Neue", Arial, sans-serif;
  }
  .poster__backdrop {
    position: absolute;
    inset: 0;
    background:
      radial-gradient(circle at 388px 290px, rgba(255,250,225,0.95) 0 82px, rgba(255,220,140,0.35) 84px, rgba(255,200,120,0) 220px),
      linear-gradient(180deg, var(--sky-top) 0%, var(--sky-mid) 40%, var(--sky-low) 70%, var(--ground) 100%);
  }
  .quote {
    position: absolute;
    right: 282px;
    margin: 0;
    text-transform: uppercase;
    white-space: nowrap;
    text-align: right;
    line-height: 1;
    letter-spacing: -0.045em;
    color: var(--ink);
    font-weight: 400;
  }
  .quote--lead { font-size: 76px; }
  .quote--lead.quote--accent { color: var(--accent); }
  .quote--close { font-size: 70px; }
  .quote__line-1 { top: 40px; left: 57px; right: auto; text-align: left; }
  .quote__line-2 { top: 116px; left: 57px; right: auto; text-align: left; }
  .quote__line-3 { top: 312px; }
  .quote__line-4 { top: 380px; }
  .quote__line-5 { top: 448px; }
  .attribution {
    position: absolute;
    right: 285px;
    top: 550px;
    margin: 0;
    font-size: 32px;
    color: var(--ink);
    white-space: nowrap;
  }
  .brand {
    position: absolute;
    left: 48px;
    bottom: 34px;
    display: flex;
    align-items: center;
    gap: 12px;
    color: var(--mark);
    font-size: 26px;
    white-space: nowrap;
  }
  .brand__square {
    width: 40px;
    height: 40px;
    background: var(--mark);
  }
</style>
</head>
<body>
  <main class="poster">
    <div class="poster__backdrop" role="img" aria-label="Sunset sky behind a cable-stayed bridge with a truck silhouette crossing over the water"></div>

    <p class="quote quote--lead quote__line-1">“It’s very difficult to</p>
    <p class="quote quote--lead quote--accent quote__line-2">follow our dreams,</p>
    <p class="quote quote--close quote__line-3">but it’s even</p>
    <p class="quote quote--close quote__line-4">more difficult</p>
    <p class="quote quote--close quote__line-5">to forget them.”</p>

    <p class="attribution">- Devan Kollur</p>

    <div class="brand">
      <span class="brand__square"></span>
      <span class="brand__name">Cornerline Driver Training</span>
    </div>
  </main>
</body>
</html>
```